Pemberton Dialworks Business Card Design

Double Sided Business Card Design for a Locksmith company specializing in Safecracking, safe & vault service.

```html
<!DOCTYPE html>
<html lang="en">
<head>
<meta charset="utf-8">
<title>Pemberton Dialworks – Business Card</title>
<link href="https://fonts.googleapis.com/css2?family=Montserrat:wght@400;500;700;800&display=swap" rel="stylesheet">
<style>
  :root {
    --stage: #4b4b4b;
    --ink-black: #000000;
    --paper: #ebebeb;
    --brand-green: #3b7d43;
    --deep-green: #1f4d2c;
    --pale-green: #a9c79a;
    --text-dark: #2b2b2b;
    --text-mid: #3c3c3c;
    --white: #ffffff;
  }
  * { margin: 0; padding: 0; box-sizing: border-box; }
  html, body { width: 1200px; height: 900px; overflow: hidden; }
  body {
    background: var(--stage);
    font-family: "Montserrat", sans-serif;
    position: relative;
  }
  .card {
    position: absolute;
    top: 288px;
    width: 540px;
    height: 324px;
    overflow: hidden;
  }
  .card--front { left: 40px; background: var(--ink-black); }
  .card--back { left: 620px; background: var(--paper); }

  .pattern { position: absolute; inset: 0; width: 100%; height: 100%; }

  .wordmark {
    position: absolute;
    display: flex;
    align-items: center;
    gap: 14px;
  }
  .wordmark__dot {
    border-radius: 50%;
    background: var(--brand-green);
    flex: none;
  }
  .wordmark__name {
    font-weight: 800;
    text-transform: uppercase;
    line-height: 1.02;
    letter-spacing: 0.5px;
  }
  .card--front .wordmark { left: 58px; top: 98px; }
  .card--front .wordmark__dot { width: 126px; height: 126px; }
  .card--front .wordmark__name { color: var(--white); font-size: 30px; }

  .card--back .wordmark { left: 34px; top: 126px; gap: 10px; }
  .card--back .wordmark__dot { width: 70px; height: 70px; }
  .card--back .wordmark__name { color: var(--brand-green); font-size: 16.5px; }

  .person { position: absolute; left: 304px; top: 60px; right: 0; }
  .person__name {
    font-size: 19px;
    color: var(--text-dark);
    letter-spacing: 0.3px;
    font-weight: 400;
    text-transform: uppercase;
  }
  .person__name strong { font-weight: 700; }
  .person__role {
    margin-top: 2px;
    font-size: 11.5px;
    line-height: 1.1;
    color: var(--brand-green);
    font-weight: 500;
  }
  .person__rule {
    position: absolute;
    left: 102px; right: 0; top: 28px;
    height: 1.3px;
    background: var(--text-dark);
  }
  .address {
    position: absolute;
    left: 304px; top: 127px;
    font-size: 11.5px;
    line-height: 1.3;
    color: var(--text-mid);
  }
  .address::after {
    content: "";
    display: block;
    width: 58px;
    height: 1px;
    background: var(--text-mid);
    margin-top: 4px;
  }
  .contacts {
    position: absolute;
    left: 304px; top: 178px;
    list-style: none;
  }
  .contacts li {
    display: flex;
    align-items: center;
    gap: 9px;
    height: 24px;
    font-size: 11.5px;
    color: var(--text-mid);
  }
  .contacts__icon {
    width: 19px; height: 19px;
    border-radius: 50%;
    background: var(--brand-green);
    display: flex; align-items: center; justify-content: center;
    flex: none;
  }
  .contacts__icon svg { width: 11px; height: 11px; }
</style>
</head>
<body>

<section class="card card--front">
  <svg class="pattern" viewBox="0 0 540 324" role="img" aria-label="Scattered green square mosaic pattern in the top-left and bottom-right corners">
    <defs>
      <linearGradient id="frontTop" x1="0" y1="0" x2="1" y2="1">
        <stop offset="0" stop-color="#2f6b3c"/>
        <stop offset="1" stop-color="#0c2413" stop-opacity="0"/>
      </linearGradient>
      <linearGradient id="frontBottom" x1="1" y1="1" x2="0" y2="0">
        <stop offset="0" stop-color="#2f6b3c"/>
        <stop offset="1" stop-color="#0c2413" stop-opacity="0"/>
      </linearGradient>
    </defs>
    <polygon points="0,0 280,0 120,70 0,110" fill="url(#frontTop)"/>
    <polygon points="540,324 300,324 420,260 540,220" fill="url(#frontBottom)"/>
  </svg>
  <div class="wordmark">
    <span class="wordmark__dot"></span>
    <span class="wordmark__name">Pemberton<br>Dialworks</span>
  </div>
</section>

<section class="card card--back">
  <svg class="pattern" viewBox="0 0 540 324" role="img" aria-label="Scattered pale green square mosaic pattern in the top-left and bottom-right corners">
    <defs>
      <linearGradient id="backTop" x1="0" y1="0" x2="1" y2="1">
        <stop offset="0" stop-color="#7fae7e"/>
        <stop offset="1" stop-color="#c9dbbf" stop-opacity="0"/>
      </linearGradient>
      <linearGradient id="backBottom" x1="1" y1="1" x2="0" y2="0">
        <stop offset="0" stop-color="#7fae7e"/>
        <stop offset="1" stop-color="#c9dbbf" stop-opacity="0"/>
      </linearGradient>
    </defs>
    <polygon points="0,0 270,0 110,70 0,110" fill="url(#backTop)"/>
    <polygon points="540,324 300,324 420,260 540,220" fill="url(#backBottom)"/>
  </svg>

  <div class="wordmark">
    <span class="wordmark__dot"></span>
    <span class="wordmark__name">Pemberton<br>Dialworks</span>
  </div>

  <div class="person">
    <h1 class="person__name"><strong>Corin</strong> Halvard</h1>
    <span class="person__rule"></span>
    <p class="person__role">Safecracking,<br>safe &amp; vault service</p>
  </div>

  <p class="address">address here, Suite#1<br>New Avenue, NY -012</p>

  <ul class="contacts">
    <li>
      <span class="contacts__icon">
        <svg viewBox="0 0 24 24"><path fill="#fff" d="M6.6 10.8a15.5 15.5 0 0 0 6.6 6.6l2.2-2.2a1 1 0 0 1 1-.25 11.4 11.4 0 0 0 3.6.6 1 1 0 0 1 1 1V20a1 1 0 0 1-1 1A17 17 0 0 1 3 4a1 1 0 0 1 1-1h3.5a1 1 0 0 1 1 1c0 1.25.2 2.45.6 3.6a1 1 0 0 1-.25 1z"/></svg>
      </span>
      123 . 456&nbsp; 78907890
    </li>
    <li>
      <span class="contacts__icon">
        <svg viewBox="0 0 24 24"><rect x="3" y="6" width="18" height="12" fill="none" stroke="#fff" stroke-width="2"/><path d="M3 6l9 7 9-7" fill="none" stroke="#fff" stroke-width="2"/></svg>
      </span>
      hello@pembertondial.com
    </li>
    <li>
      <span class="contacts__icon">
        <svg viewBox="0 0 24 24" fill="none" stroke="#fff" stroke-width="2"><circle cx="12" cy="12" r="9"/><ellipse cx="12" cy="12" rx="4" ry="9"/><path d="M3 12h18"/></svg>
      </span>
      www.pembertondial.com
    </li>
  </ul>
</section>

</body>
</html>
```